Client Proposal

I need a proposal template to give to potential clients detailing our services, safety, company history, table of contents and appendixes. I need a cover page to start with images describing our services. Our company is based in Grande Prairie, Alberta. We do land survey work, engineering and environmental.

In word format please so that we can change the proposal on an as needed basis.

```html
<!DOCTYPE html>
<html lang="en">
<head>
<meta charset="utf-8">
<title>Project Proposal Template</title>
<link href="https://fonts.googleapis.com/css2?family=Lato:wght@400;700;900&family=Roboto:wght@400;500;700&display=swap" rel="stylesheet">
<style>
  :root{
    --bg:#1d1d1f;
    --paper:#ffffff;
    --blue:#1a96cf;
    --blue-dark:#1583b8;
    --ink:#2a2a2a;
    --grey:#8b8c8f;
    --gold:#8a7431;
    --sun-top:#8a8a8c;
    --sun-mid:#d9a45c;
    --sun-low:#f3b64a;
  }
  *{margin:0;padding:0;box-sizing:border-box}
  html,body{width:667px;height:1200px;overflow:hidden;background:var(--bg)}
  body{position:relative;font-family:"Lato",sans-serif;color:var(--ink)}
  .page{position:absolute;left:190px;width:288px;height:373px;background:var(--paper);overflow:hidden}
  .page--history{top:27px}
  .page--services{top:414px}
  .page--appendix{top:800px}

  .page-title{position:absolute;left:0;right:0;top:30px;text-align:center;color:var(--blue);font-weight:700;font-size:8.4px;letter-spacing:.1px}
  .lead{position:absolute;left:44px;top:55px;width:206px;color:var(--blue);font-size:7.4px;line-height:9.2px}
  .body-copy{position:absolute;left:44px;width:200px;font-size:5px;line-height:6.2px;color:var(--ink)}
  .body-copy p+p{margin-top:6.2px}
  .col{position:absolute;width:95px;font-size:5px;line-height:6.25px;color:var(--ink)}
  .col--left{left:44px}
  .col--right{left:150px}

  .hero-photo{position:absolute;left:0;top:155px;width:288px;height:218px;
    background:linear-gradient(180deg,var(--sun-top) 0%,#b69a7d 30%,var(--sun-mid) 58%,var(--sun-low) 74%,#7a5a3a 86%,#4b3a2c 100%)}

  .footer{position:absolute;left:0;top:345px;width:288px;height:16px}
  .footer svg{position:absolute;left:0;top:0}
  .footer-brand{position:absolute;left:22px;top:4px;display:flex;align-items:center;gap:2px;color:#fff;font-weight:700;font-size:5.4px;letter-spacing:.2px}
  .footer-brand i{display:block;width:6px;height:6px;background:#fff}
  .footer-label{position:absolute;left:195px;top:4.6px;color:#fff;font-weight:900;font-size:5.6px;letter-spacing:.1px}
  .footer-num{position:absolute;left:261px;top:4.6px;color:#fff;font-weight:900;font-size:5.6px}

  .diagram{position:absolute;left:0;top:0;width:288px;height:373px;font-family:"Roboto",sans-serif}
  .box{position:absolute;background:#fff;border:.6px solid var(--blue);border-radius:2.5px;overflow:hidden}
  .box-head{background:var(--blue);color:#fff;font-weight:700;font-size:5px;letter-spacing:.2px;text-align:center;height:11px;line-height:11px}
  .box ul{list-style:none;padding:3px 0 0 6px;font-size:4.6px;line-height:6.5px;color:#333}
  .box--survey{left:44px;top:144px;width:59px;height:37px}
  .box--civil{left:44px;top:191px;width:59px;height:37px}
  .box--sectors{left:144px;top:144px;width:97px;height:85px;border-color:var(--gold)}
  .box--sectors .box-head{background:var(--gold)}
  .box--sectors ul{padding:5px 0 0 10px}
  .brand-card{position:absolute;left:144px;top:245px;width:97px;height:74px;border:.6px solid var(--blue);border-radius:4px;overflow:hidden;background:#fff}
  .brand-card-name{height:32px;display:flex;align-items:center;justify-content:center;gap:3px;color:var(--blue);font-family:"Lato",sans-serif;font-weight:700;font-size:9px;letter-spacing:.3px}
  .brand-card-name i{display:block;width:9px;height:9px;background:var(--blue)}
  .brand-card-note{height:42px;background:var(--blue);color:#fff;font-size:4.8px;line-height:5.8px;text-align:center;padding-top:9px}

  .appendix-band{position:absolute;left:0;top:0;width:288px;height:34px;background:var(--blue)}
  .appendix-band h2{position:absolute;right:22px;top:16px;color:#fff;font-weight:400;font-size:8.4px}
  .appendix-heading{position:absolute;left:78px;top:60px;color:var(--blue);font-weight:700;font-size:7.4px;line-height:9.2px}
  .appendix-copy{position:absolute;left:78px;top:88px;width:190px;color:var(--blue);font-size:5px;line-height:6.22px}
  .appendix-copy p+p{margin-top:6.2px}
</style>
</head>
<body>

<section class="page page--history">
  <h1 class="page-title">COMPANY HISTORY</h1>
  <p class="lead">Northline Surveying &amp; Engineering provides innovative, cost-effective integrated surveying and civil engineering services throughout Alberta.</p>
  <div class="body-copy" style="top:92px">
    <p>We are proud to offer professional and technical diversity and expertise, enabling us to offer a broad range of services to many industry sectors in the primary practice areas of surveying (land/legal, construction, pipeline integrity) and civil engineering (land development, transportation, municipal).</p>
    <p>From planning to management, we bring an unparalleled combination of experience, innovation and values-driven leadership to everything we do. Our approach ensures you get exactly what you asked, more than you expected and, whenever possible, faster than planned.</p>
  </div>
  <div class="hero-photo" role="img" aria-label="Photo of two surveyors on a construction site at sunset with a tower crane"></div>
  <div class="col col--left" style="top:162px">Lorem ipsum dolor sit amet, consectetur adipiscing elit. Vestibulum mattis urna metus, eu viverra ex viverra a. Praesent sit amet ex vitae enim rutrum dapibus. Mauris neque dui, tristique ut rhoncus a, feugiat quis ipsum. Praesent at ligula mi. Duis a volutpat tortor. Vestibulum eu leo ut nunc tincidunt bibendum in ut lorem. Duis eget luctus dui. Duis interdum, justo quis pretium aliquet, congue lorem at vulputate vestibulum.</div>
  <div class="col col--right" style="top:162px">Proin at nibh ut nibh lobortis pretium tempor et urna. Duis vehicula nibh in volutpat rutrum. Mauris molestie tempus nisl, ac accumsan libero ultricies sed. In dui arcu, tempor sit amet eleifend at, semper sed urna. Nulla diam ante, porttitor ut elit ac, viverra ultricies diam. Mauris odio ligula, fermentum vulputate tristique eu, vestibulum id velit. Nulla imperdiet tellus tortor, a viverra nibh semper ac.</div>
  <div class="footer">
    <svg width="288" height="16" viewBox="0 0 288 16"><polygon points="0,0 168,0 176,16 0,16" fill="#8b8c8f"/><polygon points="171,0 184,0 177.5,7" fill="#8b8c8f"/><polygon points="191,0 288,0 288,16 183,16" fill="#1a96cf"/></svg>
    <div class="footer-brand"><i></i>NORTHLINE</div>
    <div class="footer-label">PROJECT PROPOSAL</div>
    <div class="footer-num">4</div>
  </div>
</section>

<section class="page page--services">
  <h1 class="page-title">OUR SERVICES</h1>
  <div class="col col--left" style="top:63px">Lorem ipsum dolor sit amet, consectetur adipiscing elit. Vestibulum mattis urna metus, eu viverra ex viverra a. Praesent sit amet ex vitae enim rutrum dapibus. Mauris neque dui, tristique ut rhoncus a, feugiat quis ipsum. Praesent at ligula mi. Duis a volutpat tortor. Vestibulum eu leo ut nunc tincidunt bibendum in ut lorem. Duis eget luctus dui. Duis interdum, justo quis pretium aliquet, congue lorem at vulputate vestibulum.</div>
  <div class="col col--right" style="top:63px">Proin at nibh ut nibh lobortis pretium tempor et urna. Duis vehicula nibh in volutpat rutrum. Mauris molestie tempus nisl, ac accumsan libero ultricies sed. In dui arcu, tempor sit amet eleifend at, semper sed urna. Nulla diam ante, porttitor ut elit ac, viverra ultricies diam. Mauris odio ligula, fermentum vulputate tristique eu, vestibulum id velit. Nulla imperdiet tellus tortor, a viverra nibh semper ac.</div>

  <div class="diagram">
    <svg width="288" height="373" viewBox="0 0 288 373" style="position:absolute;left:0;top:0">
      <path d="M103,161 H112 Q118,161 121,168 L127,182 Q129,186 133,186 H136 M103,211 H112 Q118,211 121,204 L127,190 Q129,186 133,186" fill="none" stroke="#8b8c8f" stroke-width="4.5"/>
      <polygon points="134,180 144,186 134,192" fill="#8b8c8f"/>
      <polygon points="186,233 200,233 193,242" fill="#8b8c8f"/>
    </svg>
    <div class="box box--survey">
      <div class="box-head">SURVEYING</div>
      <ul><li>· Land/Legal</li><li>· Construction</li><li>· Pipeline Integrity</li></ul>
    </div>
    <div class="box box--civil">
      <div class="box-head">CIVIL ENGINEERING</div>
      <ul><li>· Land Development</li><li>· Transportation</li><li>· Municipal</li></ul>
    </div>
    <div class="box box--sectors">
      <div class="box-head">INDUSTRY SECTORS</div>
      <ul>
        <li>· Public Works</li><li>· Transportation</li><li>· Oil and Gas</li><li>· Resource Development</li><li>· Real Estate and Residential</li><li>· Utilities and Transmission</li><li>· Telecommunications</li><li>· Pipeline and Heavy Construction</li><li>· Municipal, Industrial Development</li>
      </ul>
    </div>
    <div class="brand-card">
      <div class="brand-card-name"><i></i>NORTHLINE</div>
      <div class="brand-card-note">Multiple Products and Services<br>for each practice area and<br>industry sector/</div>
    </div>
  </div>

  <div class="footer">
    <svg width="288" height="16" viewBox="0 0 288 16"><polygon points="0,0 168,0 176,16 0,16" fill="#8b8c8f"/><polygon points="171,0 184,0 177.5,7" fill="#8b8c8f"/><polygon points="191,0 288,0 288,16 183,16" fill="#1a96cf"/></svg>
    <div class="footer-brand"><i></i>NORTHLINE</div>
    <div class="footer-label">PROJECT PROPOSAL</div>
    <div class="footer-num">5</div>
  </div>
</section>

<section class="page page--appendix">
  <div class="appendix-band"><h2>Appendixes</h2></div>
  <h3 class="appendix-heading">Lorem ipsum dolor sit amet<br>consectetur adipiscing eli</h3>
  <div class="appendix-copy">
    <p>Lorem ipsum dolor sit amet, consectetur adipiscing elit. Vestibulum mattis urna metus, eu viverra ex viverra a. Praesent sit amet ex vitae enim rutrum dapibus. Mauris neque dui, tristique ut rhoncus a, feugiat quis ipsum. Praesent at ligula mi. Duis a volutpat tortor. Vestibulum eu leo ut nunc tincidunt bibendum in ut lorem. Duis eget luctus dui. Duis interdum, justo quis pretium aliquet, felis justo posuere urna, ut suscipit elit ligula eget orci. Ut congue lorem at vulputate vestibulum.</p>
    <p>Proin at nibh ut nibh lobortis pretium tempor et urna. Duis vehicula nibh in volutpat rutrum. Mauris molestie tempus nisl, ac accumsan libero ultricies sed. In dui arcu, tempor sit amet eleifend at, semper sed urna. Nulla diam ante, porttitor ut elit ac, viverra ultricies diam. Mauris odio ligula, fermentum vulputate tristique eu, vestibulum id velit. Nulla imperdiet tellus tortor, a viverra nibh semper ac. Donec tempus velit quis erat dignissim lacinia. Integer tortor est, efficitur a eleifend nec, tincidunt eu nunc.</p>
    <p>Aenean et leo id enim gravida volutpat sed ut leo. Nunc pretium tortor id urna egestas faucibus. Quisque non tincidunt ex. Sed iaculis aliquet rutrum. Proin fringilla viverra diam, non congue neque hendrerit quis. Fusce convallis est ac nunc sollicitudin, id maximus massa consectetur. Nullam tempus, augue et faucibus ultricies, libero nisl tristique mauris, vel pulvinar odio risus nec risus. Vestibulum ante ipsum primis in faucibus orci luctus et ultrices posuere cubilia curae; Curabitur eu tellus non eros cursus feugiat. Sed rutrum risus id lacus tristique, ut condimentum velit convallis. Proin vitae feugiat purus, ut scelerisque ante. Morbi vitae lacus quam. Pellentesque maximus eros sed eros aliquam, id tincidunt ex hendrerit. Proin convallis interdum orci quis fermentum. Nunc id tristique arcu. Duis placerat velit et est lacinia, vel consectetur est cursus.</p>
    <p>Cras commodo ligula nec tempor mollis. Sed commodo metus imperdiet risus ullamcorper, id interdum massa condimentum. Donec malesuada libero at finibus tristique. Aenean nisi est, scelerisque in lectus a, fringilla ornare nulla. Proin vitae quam orci. Etiam semper vel lacus a lobortis. Sed id dolor nec neque convallis dignissim id id neque. Aenean eros nisi, laoreet et pharetra quis, cursus quis erat. Sed odio quam, pretium et interdum sit amet, ultrices ac turpis. Nullam scelerisque sem eget felis vulputate, in varius eros vehicula. Pellentesque accumsan mattis magna sit amet pellentesque.</p>
  </div>
  <div class="footer">
    <svg width="288" height="16" viewBox="0 0 288 16"><polygon points="0,0 168,0 176,16 0,16" fill="#8b8c8f"/><polygon points="171,0 184,0 177.5,7" fill="#8b8c8f"/><polygon points="191,0 288,0 288,16 183,16" fill="#1a96cf"/></svg>
    <div class="footer-brand"><i></i>NORTHLINE</div>
    <div class="footer-label">PROJECT PROPOSAL</div>
    <div class="footer-num">6</div>
  </div>
</section>

</body>
</html>
```